harvest Soon Book Cover Design for real estate investment book

I am looking for a Book Cover design for my new book. I would like designs for a hardcover, softcover and Lumora book.

The book deals with real estate and mortgage investments. Looking for a clean, bright simple design. Want to cover to be White with big RED letters. See "Dancing past Noon" book for an example ... see attached.

Target Market(s)

Affluent people with money looking for investment solutions.

Industry/Entity Type

Financial Service

Font styles to use
Serif

Requirements
Must have
• Bright clean design that will be appealing to affluent people.
• Title: harvest SOON
• Subtitle: A quiet method for thriving through land holdings
• subsubtitle: Secrets the Bank Teller Keeps Hidden From Clients...
• Author: Ned Falconby
• My Picture on the inside cover or on the back cover
• Book Description, Author description
Nice to have
• Focus on the Front cover look and feel first. Then we can look at the inside flaps and back cover. I will need to send you text. This is for the full cover. Front. Back. Spine. Inside flaps fro hardcover.

```html
<!DOCTYPE html>
<html lang="en">
<head>
<meta charset="utf-8">
<title>harvest SOON – Full Book Cover</title>
<link rel="stylesheet" href="https://fonts.googleapis.com/css2?family=Montserrat:wght@400;500;700;900&display=swap">
<style>
  :root {
    --paper: #ffffff;
    --ink: #141414;
    --body-ink: #3a3a3a;
    --title-red: #c8161e;
    --tagline-red: #a3191d;
    --trim: #b9b9b9;
    --photo-dark: #2c3340;
    --photo-mid: #8a95a6;
    --photo-light: #c9d0da;
  }
  html, body {
    margin: 0;
    padding: 0;
    width: 1200px;
    height: 1200px;
    overflow: hidden;
    background: var(--paper);
  }
  .cover-canvas {
    display: block;
    width: 1200px;
    height: 1200px;
    font-family: "Montserrat", sans-serif;
  }
  .trim-line { fill: none; stroke: var(--trim); stroke-width: 1.2; }
  .heading { font-weight: 700; font-size: 13px; fill: var(--ink); }
  .body-copy { font-weight: 400; font-size: 10.5px; fill: var(--body-ink); }
  .photo-slot { fill: none; stroke: var(--ink); stroke-width: 1.4; }
  .crop-mark { fill: none; stroke: var(--ink); stroke-width: 1.4; }
  .spine-author { font-weight: 500; font-size: 19px; fill: var(--ink); letter-spacing: 1px; }
  .title { font-weight: 900; font-size: 140px; fill: var(--title-red); }
  .subtitle { font-weight: 900; font-size: 27px; fill: var(--ink); }
  .tagline { font-weight: 900; font-size: 13px; fill: var(--tagline-red); }
  .front-author { font-weight: 500; font-size: 31px; fill: var(--ink); letter-spacing: 1px; }
</style>
</head>
<body>
<svg class="cover-canvas" viewBox="0 0 1200 1200" xmlns="http://www.w3.org/2000/svg">
  <defs>
    <linearGradient id="heroTones" x1="0" y1="0" x2="1" y2="1">
      <stop offset="0" stop-color="var(--photo-mid)"/>
      <stop offset="0.45" stop-color="var(--photo-light)"/>
      <stop offset="0.75" stop-color="var(--photo-mid)"/>
      <stop offset="1" stop-color="var(--photo-dark)"/>
    </linearGradient>
  </defs>

  <!-- full wrap trim -->
  <g class="wrap-trim">
    <rect class="trim-line" x="37" y="216" width="1127" height="778"/>
    <line class="trim-line" x1="558" y1="216" x2="558" y2="994"/>
    <line class="trim-line" x1="646" y1="216" x2="646" y2="994"/>
  </g>

  <!-- back cover -->
  <g class="back-cover">
    <text class="heading" x="112" y="301">BOOK DESCRIPTION:</text>
    <g class="body-copy">
      <text x="112" y="321" textLength="338">book description book description book description book description</text>
      <text x="112" y="337" textLength="338">book description book description book description book description</text>
      <text x="112" y="352" textLength="338">book description book description book description book description</text>
      <text x="112" y="368" textLength="338">book description book description book description book description</text>
      <text x="112" y="383" textLength="338">book description book description book description book description</text>
      <text x="112" y="399" textLength="338">book description book description book description book description</text>
      <text x="112" y="415" textLength="338">book description book description book description book description</text>
      <text x="112" y="430" textLength="338">book description book description book description book description</text>
      <text x="112" y="446" textLength="338">book description book description book description book description</text>
      <text x="112" y="461" textLength="338">book description book description book description book description</text>
      <text x="112" y="477">book description book description.</text>
    </g>

    <rect class="photo-slot" x="80" y="552" width="65" height="64" role="img" aria-label="Author portrait placeholder"/>

    <text class="heading" x="80" y="645">AUTHOR DESCRIPTION:</text>
    <g class="body-copy">
      <text x="80" y="662" textLength="185">Author description Author description</text>
      <text x="80" y="678" textLength="185">Author description Author description</text>
      <text x="80" y="693" textLength="185">Author description Author description</text>
      <text x="80" y="709" textLength="185">Author description Author description</text>
      <text x="80" y="724" textLength="185">Author description Author description</text>
      <text x="80" y="740" textLength="185">Author description Author description</text>
      <text x="80" y="755" textLength="185">Author description Author description</text>
      <text x="80" y="771" textLength="185">Author description Author description</text>
      <text x="80" y="787" textLength="185">Author description Author description</text>
      <text x="80" y="802" textLength="185">Author description Author description</text>
      <text x="80" y="818" textLength="185">Author description Author description</text>
      <text x="80" y="833" textLength="185">Author description Author description</text>
      <text x="80" y="849" textLength="185">Author description Author description</text>
      <text x="80" y="864">Author .</text>
    </g>
  </g>

  <!-- spine -->
  <g class="spine">
    <text class="spine-author" transform="translate(595 252) rotate(90)" textLength="202">AUTHOR: NED FALCONBY</text>
    <g class="crop-mark">
      <polyline points="569,484 569,470 583,470"/>
      <polyline points="618,470 632,470 632,484"/>
      <polyline points="569,519 569,533 583,533"/>
      <polyline points="618,533 632,533 632,519"/>
    </g>
  </g>

  <!-- hero image band spanning back and front -->
  <rect x="300" y="550" width="864" height="390" fill="url(#heroTones)" role="img"
        aria-label="Photograph of many pale sculpted hands reaching upward, one holding a bowl of coins and banknotes"/>

  <!-- front cover -->
  <g class="front-cover">
    <text class="title" x="658" y="348" textLength="492" lengthAdjust="spacingAndGlyphs">HARVEST</text>
    <text class="title" x="700" y="446" textLength="410" lengthAdjust="spacingAndGlyphs">SOON</text>
    <text class="subtitle" x="660" y="490" textLength="488" lengthAdjust="spacingAndGlyphs">A QUIET METHOD FOR THRIVING</text>
    <text class="subtitle" x="660" y="518" textLength="488" lengthAdjust="spacingAndGlyphs">THROUGH LAND HOLDINGS</text>
    <text class="tagline" x="660" y="537" textLength="488" lengthAdjust="spacingAndGlyphs">SECRETS THE BANK TELLER KEEPS HIDDEN FROM CLIENTS...</text>
    <text class="front-author" x="658" y="977" textLength="260">NED FALCONBY</text>
  </g>
</svg>
</body>
</html>
```